Ebook cover design for SPY THRILLER

An eBook cover is needed for a spy thriller. Good books to reference are Morgan Frewley and Oliver Trenchard. We are after something cutting-edge, dramatic, stylish, and that stands out above the rest.

Title: The Copper Heron: Hollow Meridian (The Copper Heron is the series).
Author: Gregory Velunde

The book is about a spy who goes undercover to stop an organ harvesting operation in Hungary. The name Gregory can be in white, and Velunde in shiny gold. Also feel free to make "The Copper Heron" in shiny gold as well, and "Hollow Meridian" in any way you think will look good (i.e. Red). Thick font would be good.

The winner of this will also have the privlege of creating the next 6 covers in the series, as they come about.

This project is suitable for designers who have experience creating eBook covers to Pellworth's standard, and enjoy creating new, stand-out designs which really help the book stand tall above the rest.

```html
<!DOCTYPE html>
<html lang="en">
<head>
<meta charset="utf-8">
<title>The Copper Heron: Hollow Meridian — Gregory Velunde</title>
<link rel="stylesheet" href="https://fonts.googleapis.com/css2?family=Cinzel:wght@700;900&family=Russo+One&display=swap">
<style>
  :root {
    --ink: #000000;
    --gold-light: #fff4c4;
    --gold-mid: #e6b445;
    --gold-deep: #94640e;
    --red-light: #ffe2e6;
    --red-mid: #f0707c;
    --red-deep: #d6303c;
    --sky-pale: #ecebc0;
    --sky-mid: #9a9768;
    --sky-dim: #4a4933;
    --sky-dark: #15150e;
  }
  html, body {
    margin: 0;
    padding: 0;
    width: 750px;
    height: 1200px;
    overflow: hidden;
    background: var(--ink);
  }
  .cover {
    position: relative;
    width: 750px;
    height: 1200px;
    background: var(--ink);
    overflow: hidden;
  }
  .cover-art {
    position: absolute;
    inset: 0;
    width: 750px;
    height: 1200px;
    display: block;
  }
  .series-title,
  .author-name {
    font-family: "Cinzel", "Times New Roman", serif;
    font-weight: 900;
  }
  .book-title {
    font-family: "Russo One", "Arial Black", sans-serif;
  }
</style>
</head>
<body>
  <main class="cover">
    <svg class="cover-art" viewBox="0 0 750 1200" width="750" height="1200" aria-labelledby="cover-title">
      <title id="cover-title">The Copper Heron: Hollow Meridian by Gregory Velunde</title>
      <defs>
        <linearGradient id="gold-sheen" x1="0" y1="0" x2="0" y2="1">
          <stop offset="0" stop-color="var(--gold-deep)"/>
          <stop offset="0.3" stop-color="var(--gold-mid)"/>
          <stop offset="0.55" stop-color="var(--gold-light)"/>
          <stop offset="0.8" stop-color="var(--gold-mid)"/>
          <stop offset="1" stop-color="var(--gold-deep)"/>
        </linearGradient>
        <radialGradient id="red-sheen" gradientUnits="userSpaceOnUse" cx="375" cy="260" r="380">
          <stop offset="0" stop-color="var(--red-light)"/>
          <stop offset="0.3" stop-color="var(--red-mid)"/>
          <stop offset="1" stop-color="var(--red-deep)"/>
        </radialGradient>
        <linearGradient id="dusk-sky" x1="0" y1="0" x2="0" y2="1">
          <stop offset="0" stop-color="var(--ink)"/>
          <stop offset="0.2" stop-color="var(--sky-dark)"/>
          <stop offset="0.42" stop-color="var(--sky-dim)"/>
          <stop offset="0.56" stop-color="var(--sky-mid)"/>
          <stop offset="0.63" stop-color="var(--sky-pale)"/>
          <stop offset="0.7" stop-color="var(--sky-dim)"/>
          <stop offset="0.76" stop-color="var(--sky-dark)"/>
          <stop offset="0.86" stop-color="var(--ink)"/>
          <stop offset="1" stop-color="var(--ink)"/>
        </linearGradient>
        <radialGradient id="dusk-glow" gradientUnits="userSpaceOnUse" cx="640" cy="700" r="260">
          <stop offset="0" stop-color="var(--sky-pale)" stop-opacity="0.75"/>
          <stop offset="0.5" stop-color="var(--sky-mid)" stop-opacity="0.3"/>
          <stop offset="1" stop-color="var(--sky-mid)" stop-opacity="0"/>
        </radialGradient>
      </defs>

      <g class="skyline" role="img" aria-label="Dusk city skyline with church spires and towers in silhouette under dark, brooding clouds">
        <rect x="0" y="540" width="750" height="350" fill="url(#dusk-sky)"/>
        <rect x="300" y="560" width="450" height="230" fill="url(#dusk-glow)"/>
      </g>

      <text class="series-title" x="376" y="119" text-anchor="middle" font-size="68"
            textLength="670" lengthAdjust="spacingAndGlyphs" fill="url(#gold-sheen)">THE COPPER HERON</text>

      <g class="book-title" fill="url(#red-sheen)">
        <text x="378" y="280" text-anchor="middle" font-size="182"
              textLength="580" lengthAdjust="spacingAndGlyphs">HOLLOW</text>
        <text x="375" y="443" text-anchor="middle" font-size="182"
              textLength="668" lengthAdjust="spacingAndGlyphs">MERIDIAN</text>
      </g>

      <g class="author-name" fill="url(#gold-sheen)">
        <text x="375" y="1002" text-anchor="middle" font-size="104"
              textLength="640" lengthAdjust="spacingAndGlyphs">GREGORY</text>
        <text x="392" y="1107" text-anchor="middle" font-size="104"
              textLength="580" lengthAdjust="spacingAndGlyphs">VELUNDE</text>
      </g>
    </svg>
  </main>
</body>
</html>
```